Norvane Builders Business Card

Modern and Professional Business Card for a Med size construction/development company.

See the samples below for the design I like … but I need ideas for incorporating the red company logo while still keeping the clean look of the card samples that are attached.

Logo and tag line on the back … info on the front.

Tagline: Quality Starts from the Ground Up

Target Market(s)

Med-Large General Contractors

Contact Information for Business Card

Norvane Builders Limited
42 Brenton Street
Elk Harbour, NL
B3K 7T2

t: 709-555-0147
f: 709-555-0192
w: www.norvanebuilders-example.com

Font styles to use
Sans Serif

Colors
fbee3e

Requirements
Must have
• I like the black and yellow designs of the attached samples …. but I'm not sure how to incorporate the red Norvane Builders logo into that design??
Nice to have
• Construction safety strips

```html
<!DOCTYPE html>
<html lang="en">
<head>
<meta charset="utf-8">
<title>Norvane Builders Business Card</title>
<link rel="stylesheet" href="https://fonts.googleapis.com/css2?family=Arimo:ital,wght@0,700;1,400&family=Montserrat:wght@400;700&display=swap">
<style>
  :root {
    --backdrop: #8c8982;
    --card: #ffffff;
    --charcoal: #4a4a4a;
    --ink: #3d3d3d;
    --safety-yellow: #fbee3e;
    --brand-red: #c8202a;
    --rule: #c4c4c4;
  }
  * { margin: 0; padding: 0; box-sizing: border-box; }
  html, body { width: 1200px; height: 1200px; overflow: hidden; }
  body { background: var(--backdrop); position: relative; font-family: "Montserrat", sans-serif; }

  .card { position: absolute; background: var(--card); }
  .card-back-face { left: 257px; top: 122px; width: 695px; height: 413px; }
  .card-info-face { left: 258px; top: 620px; width: 697px; height: 418px; }

  .safety-stripes {
    position: absolute;
    background: repeating-linear-gradient(-45deg, var(--safety-yellow) 0 10px, var(--charcoal) 10px 20px);
  }

  /* Logo side */
  .logo-panel {
    position: absolute; left: 22px; top: 20px; width: 651px; height: 372px;
    background: var(--charcoal); overflow: hidden;
  }
  .wordmark {
    position: absolute; left: 0; width: 100%;
    display: flex; align-items: center; justify-content: center;
    font-family: "Arimo", sans-serif; font-weight: 700; color: var(--card);
    line-height: 1;
  }
  .brand-square { display: inline-block; background: var(--brand-red); flex: none; }
  .logo-panel .wordmark-main { top: 103px; font-size: 72px; letter-spacing: 1px; }
  .logo-panel .wordmark-main .brand-square { width: 22px; height: 22px; margin-right: 18px; }
  .logo-panel .wordmark-sub { top: 200px; font-size: 30px; letter-spacing: 3px; }
  .tagline {
    position: absolute; left: 132px; top: 290px; width: 387px; height: 32px;
    background: var(--safety-yellow); color: var(--ink);
    font-family: "Arimo", sans-serif; font-style: italic; font-weight: 400;
    font-size: 19px; line-height: 32px; text-align: center; letter-spacing: 0.3px;
  }
  .logo-panel .safety-stripes { left: 0; bottom: 0; width: 100%; height: 20px; }

  /* Info side */
  .arrow-panel { position: absolute; left: 0; top: 0; }
  .info-wordmark { position: absolute; left: 21px; width: 330px;
    display: flex; align-items: center; justify-content: center;
    font-family: "Arimo", sans-serif; font-weight: 700; color: var(--card); line-height: 1; }
  .info-wordmark.main { top: 160px; font-size: 46px; letter-spacing: 0.5px; }
  .info-wordmark.main .brand-square { width: 14px; height: 14px; margin-right: 12px; }
  .info-wordmark.sub { top: 236px; font-size: 20px; letter-spacing: 2px; }
  .card-info-face .safety-stripes { left: 21px; top: 379px; width: 258px; height: 18px; }

  .contact { position: absolute; left: 395px; top: 106px; color: var(--ink); }
  .contact-name { font-weight: 700; font-size: 17px; letter-spacing: 0.3px; line-height: 1; }
  .contact-role { font-size: 12.5px; margin-top: 6px; line-height: 1; }
  .name-rule { width: 36px; height: 3px; background: var(--brand-red); margin-top: 6px; }

  .detail { position: absolute; left: 0; font-size: 13.5px; line-height: 16.5px; padding-left: 31px; white-space: nowrap; }
  .detail .icon {
    position: absolute; left: 0; top: 1px; width: 15px; height: 15px;
    border-radius: 50%; background: var(--safety-yellow);
  }
  .detail .icon svg { display: block; width: 15px; height: 15px; }
  .detail-address { top: 56px; }
  .detail-phone { top: 131px; }
  .detail-fax { top: 155px; }
  .detail-email { top: 176px; }
  .detail-web { top: 197px; }
  .icon-rail {
    position: absolute; left: 7px; top: 140px; width: 1px; height: 66px; background: var(--rule);
  }
</style>
</head>
<body>

  <section class="card card-back-face" aria-label="Card back: name and tagline">
    <div class="logo-panel">
      <div class="wordmark wordmark-main"><span class="brand-square"></span>NORVANE</div>
      <div class="wordmark wordmark-sub">BUILDERS LIMITED</div>
      <div class="tagline">Quality Starts from the Ground Up</div>
      <div class="safety-stripes"></div>
    </div>
  </section>

  <section class="card card-info-face" aria-label="Card front: contact details">
    <svg class="arrow-panel" width="697" height="418" viewBox="0 0 697 418" aria-hidden="true">
      <polygon points="21,20 279,20 369,209 279,397 21,397" fill="var(--charcoal)"/>
      <polyline points="285,20 375,209 285,397" fill="none" stroke="var(--safety-yellow)" stroke-width="4"/>
    </svg>
    <div class="info-wordmark main"><span class="brand-square"></span>NORVANE</div>
    <div class="info-wordmark sub">BUILDERS LIMITED</div>
    <div class="safety-stripes"></div>

    <div class="contact">
      <div class="contact-name">DARA WELLS</div>
      <div class="contact-role">General Contractors</div>
      <div class="name-rule"></div>

      <div class="icon-rail"></div>

      <div class="detail detail-address">
        <span class="icon"><svg viewBox="0 0 15 15"><path d="M7.5 3.2a2.6 2.6 0 0 0-2.6 2.6c0 2 2.6 5 2.6 5s2.6-3 2.6-5a2.6 2.6 0 0 0-2.6-2.6zm0 3.6a1 1 0 1 1 0-2 1 1 0 0 1 0 2z" fill="#222"/></svg></span>
        Norvane Builders Limited<br>42 Brenton Street, Elk Harbour,<br>NL B3K 7T2
      </div>
      <div class="detail detail-phone">
        <span class="icon"><svg viewBox="0 0 15 15"><path d="M4.6 3.6l1.5-.3.9 2-1 .8c.5 1.1 1.3 1.9 2.4 2.4l.8-1 2 .9-.3 1.5c-3.5.2-6.5-2.8-6.3-6.3z" fill="#222"/></svg></span>
        709-555-0147
      </div>
      <div class="detail detail-fax">
        <span class="icon"><svg viewBox="0 0 15 15"><rect x="4" y="6" width="7" height="5" fill="#222"/><rect x="5.5" y="3.5" width="3.5" height="3" fill="#222"/></svg></span>
        709-555-0192
      </div>
      <div class="detail detail-email">
        <span class="icon"><svg viewBox="0 0 15 15"><rect x="4" y="5" width="7" height="5" rx="0.6" fill="#222"/></svg></span>
        info@norvanebuilders-example.com
      </div>
      <div class="detail detail-web">
        <span class="icon"><svg viewBox="0 0 15 15"><circle cx="7.5" cy="7.5" r="3.3" fill="none" stroke="#222" stroke-width="1"/><path d="M4.2 7.5h6.6M7.5 4.2c-1.5 2-1.5 4.6 0 6.6M7.5 4.2c1.5 2 1.5 4.6 0 6.6" fill="none" stroke="#222" stroke-width="0.8"/></svg></span>
        www.norvanebuilders-example.com
      </div>
    </div>
  </section>

</body>
</html>
```